Website design for headhunting agency

The design I need (PSD file) is for a company offering specialised services in recruitment of high-end executive and management positions for businesses.
OBJECTIVES OF THE WEBSITE:
1. Let entrepreneurs and business leaders know about their services and easily have them contact Velnarix if they want more information about their services.
2. Display a list of available carreer opportunities (according to their client's need).
WHAT I NEED:
1st, I need the design for the Home Page ONLY. Once approved, I will need the other pages designed as well. (Here is prototype that we've already developed for the Website that will guide you in the design:
http://demo.quorvaweb.example/velnarix/fr/accueil)
ATTACHED FILES
- Logo
- PDF brochure: Use for inspiration. It is encouraged that you use pictures from this brochure. You can always suggest new ones, as long as they are not expensive to buy and have the same look and feel as the brochure.
HOMEPAGE:
1. Main menu : 6 sections
Accueil | Velnarix | Équipe | Approche | Postes disponibles | Publications
2. Main slider: 4 sections
- Chasseurs de têtes (Headhunters)
- Notre approche (Our Approach)
- Postes cadres disponibles (Executive Careers
Opportunities)
- Contactez-nous (Contact Us)
3. Main Call To Action Boxes :
- Liste Des postes disponibles (Liste of Available Careers
Opportunities)
- Formulaire de contact (contact form)
4. Latest blog articles
- Les derniers articles.
OTHER PAGES (to design once Homepage is approved)
- Velnarix (about us)
- Équipe (our team)
- Approche (our approach)
- Postes disponibles (Career opportunities)
- Publications (blog articles)
- Contact (Contact us)
Target Market(s)
ORGANIZATIONS:
Leaders of organizations seeking to recruit highly qualified staff.
HIGHLY QUALIFIED RESOURCES:
Senior individuals seeking a salary between $70,000 and $ $200,000 annually
PROFESSIONAL SECTORS:
manufacturing : Primary and secondary industries
pharmaceutical
Aerospace
Finances
Retail business
Engineering
Chemical and petrochemical
IT, telecommunications and high technology
Professional Organizations and Association
Industry/Entity Type
Business
Look and feel
Each slider illustrates characteristics of the customer's brand and the style your logo design should communicate.

```html
<!DOCTYPE html>
<html lang="fr">
<head>
<meta charset="utf-8">
<title>Velnarix – Recherche de cadres</title>
<link rel="stylesheet" href="https://fonts.googleapis.com/css2?family=Arimo:wght@400;700&family=Carlito:wght@700&display=swap">
<style>
:root{
  --navy:#0d4a73;
  --navy-text:#13517a;
  --gold:#d9a825;
  --panel:#e6ebf2;
  --panel-border:#cfd7e1;
  --soft:#f7f7f7;
  --body-text:#555c63;
  --dark-text:#333;
  --link:#0d4a73;
}
*{box-sizing:border-box;margin:0;padding:0}
html,body{width:847px;height:1200px;overflow:hidden;background:#fff}
body{position:relative;font-family:"Arimo",Arial,sans-serif;color:var(--dark-text)}
.abs{position:absolute}

.topbar{left:0;top:0;width:847px;height:30px;background:var(--navy);border-bottom:2px solid var(--gold)}
.topbar a{position:absolute;top:9px;color:#fff;font-size:9px;font-weight:700;text-decoration:none}
.lang-caret{display:inline-block;margin-left:3px;border:3.5px solid transparent;border-top:5px solid #9fb3c4;vertical-align:-3px}

.header{left:0;top:32px;width:847px;height:68px;background:#fff}
.brand{left:78px;top:24px;font-family:"Arimo",Arial,sans-serif;font-size:19px;font-weight:400;color:var(--navy);letter-spacing:.5px}
.brand-mark{left:138px;top:8px;width:12px;height:12px;background:#c7ccd2}
.brand-tag{left:124px;top:45px;font-size:7.5px;color:#777}
.mainnav{left:350px;top:33px;display:flex;height:30px;align-items:center}
.mainnav a{font-size:9px;font-weight:700;color:var(--dark-text);text-decoration:none;padding:0 9px;line-height:30px;border-left:1px solid #eceef0;white-space:nowrap}
.mainnav a:first-child{border-left:0;color:var(--navy)}

.hero{left:0;top:100px;width:847px;height:302px;background:linear-gradient(90deg,#eef1f3 0%,#e3e9ee 40%,#eef3f6 70%,#e8edf1 100%);border-bottom:2px solid var(--gold)}
.hero-backdrop{left:90px;top:40px;width:300px;height:250px;background:radial-gradient(ellipse at center,#d8dde2 0%,rgba(230,234,238,0) 70%)}
.hero-photo{left:512px;top:12px;width:192px;height:290px;background:linear-gradient(180deg,#c9b8a8 0%,#7d7f8a 30%,#5d6170 70%,#4c505d 100%);border-radius:90px 90px 0 0}
.hero-title{left:119px;top:75px;font-family:"Arimo",Arial,sans-serif;font-size:18px;font-weight:700;color:var(--navy-text);letter-spacing:.2px}
.hero-text{left:120px;top:106px;width:260px;font-size:8.6px;line-height:14px;color:#333}
.hero-text a{display:block;font-weight:700;color:var(--navy);text-decoration:none}
.hero-arrow{width:20px;height:20px;border-radius:50%;background:#fff;border:1px solid #c9ced3;box-shadow:0 1px 2px rgba(0,0,0,.2)}

.cta-band{left:0;top:404px;width:847px;height:246px;background:var(--soft)}
.panel{top:438px;height:168px;background:var(--panel);border:1px solid var(--panel-border)}
.panel h2{position:absolute;left:16px;top:15px;font-family:"Carlito",Calibri,sans-serif;font-size:12px;color:var(--navy-text);font-weight:700}
.jobs{position:absolute;left:15px;top:41px;width:308px;list-style:none}
.jobs li{height:21.3px;line-height:21px;font-size:8.8px;font-weight:700;color:#3a3f44;border-bottom:1px solid #d3dae3;padding-left:16px;position:relative}
.jobs li:last-child{border-bottom:0}
.jobs li:first-child{color:var(--navy)}
.jobs li::before{content:"+";position:absolute;left:0;top:6px;width:7px;height:7px;border:1px solid #9aa4ae;background:#fff;font-size:7px;line-height:6px;text-align:center;color:#666;font-weight:400}
.form-label{font-size:8.5px;color:#555}
.field{background:#fff;border:1px solid #c7d0da}
.submit{left:678px;top:584px;width:67px;height:18px;background:linear-gradient(#3a8fd0,#1a63a5);border:1px solid #144f86;border-radius:2px;color:#fff;font-size:6.5px;font-weight:700;text-align:center;line-height:16px}

.articles-title{left:0;top:665px;width:858px;text-align:center;font-family:"Carlito",Calibri,sans-serif;font-size:12px;font-weight:700;color:var(--navy-text)}
.card{width:323px;height:139px;background:#fff;border:1px solid #ebedef;box-shadow:0 4px 6px rgba(0,0,0,.04)}
.card-photo{position:absolute;left:8px;top:22px;width:145px;height:96px}
.card h3{position:absolute;left:165px;top:26px;font-size:8.5px;font-weight:700;color:var(--navy)}
.card p{position:absolute;left:165px;top:44px;width:152px;font-size:8.2px;line-height:11.3px;color:#777}
.card p a{color:var(--link);text-decoration:none}

.follow-band{left:0;top:1040px;width:847px;height:100px;background:var(--soft)}
.follow{top:1066px;width:302px;height:44px;background:#fff;border:1px solid #e2e4e7;font-size:8.3px;color:#777}
.follow span{position:absolute;top:17px}

.footer{left:0;top:1140px;width:847px;height:38px;background:var(--navy);border-top:2px solid var(--gold)}
.footer p{position:absolute;left:98px;top:12px;font-size:8.5px;color:#fff}
.social{position:absolute;top:10px;width:14px;height:14px;border-radius:50%;background:#0a2f49}
</style>
</head>
<body>

<nav class="abs topbar" aria-label="Liens utilitaires">
  <a style="left:482px">Accueil</a>
  <a style="left:525px">Plan du site</a>
  <a style="left:584px">Code d'étique</a>
  <a style="left:652px">Contact</a>
  <a style="left:721px">English<span class="lang-caret"></span></a>
</nav>

<header class="abs header">
  <div class="abs brand-mark"></div>
  <div class="abs brand">VELNARIX</div>
  <div class="abs brand-tag">Recherche de cadres</div>
  <nav class="abs mainnav" aria-label="Navigation principale">
    <a>ACCUEIL</a><a>VELNARIX</a><a>ÉQUIPE</a><a>APPROCHE</a><a>POSTES DISPONIBLES</a><a>PUBLICATIONS</a>
  </nav>
</header>

<section class="abs hero">
  <div class="abs hero-backdrop" role="img" aria-label="Arrière-plan flou de collègues dans un bureau lumineux"></div>
  <div class="abs hero-photo" role="img" aria-label="Photo d'une femme d'affaires en veston rayé"></div>
  <h1 class="abs hero-title">CHASSEURS DE TÊTES</h1>
  <div class="abs hero-text">Doloremque laudantium, totam rem eaque ipsa quae ab illo inven-tore veritatis et quasi architecto beaae vitae dicta sunt explicabo. Nemo enim ipvoluptatem quia voluptas sit aspernatur aut odit aut fugit, sed quia consequuntur magni dolores eos qui ration<a>Read more..</a></div>
  <svg class="abs hero-arrow" style="left:77px;top:151px" viewBox="0 0 20 20"><path d="M11.5 6 L7.5 10 L11.5 14" fill="none" stroke="#333" stroke-width="2"/></svg>
  <svg class="abs hero-arrow" style="left:741px;top:151px" viewBox="0 0 20 20"><path d="M8.5 6 L12.5 10 L8.5 14" fill="none" stroke="#333" stroke-width="2"/></svg>
</section>

<div class="abs cta-band"></div>

<section class="abs panel" style="left:84px;width:324px">
  <h2>LISTE DES POSTES DISPONIBLES</h2>
  <ul class="jobs">
    <li>Nemo enim ipvoluptatem quia</li>
    <li>Enim ipvoluptatem quia voluptas sit aspernatur aut</li>
    <li>Odit aut fugit, sed quia consequuntur magni</li>
    <li>Dolores eos qui ration</li>
    <li>Enim ipvoluptatem quia voluptas sit aspernatur aut</li>
  </ul>
</section>

<section class="abs panel" style="left:430px;width:325px">
  <h2>FORMULAIRE DE CONTACT</h2>
</section>
<span class="abs form-label" style="left:449px;top:482px">Name</span>
<span class="abs form-label" style="left:604px;top:482px">Email</span>
<span class="abs form-label" style="left:449px;top:511px">Phone</span>
<span class="abs form-label" style="left:604px;top:511px">Office</span>
<div class="abs field" style="left:480px;top:474px;width:113px;height:25px"></div>
<div class="abs field" style="left:633px;top:474px;width:113px;height:25px"></div>
<div class="abs field" style="left:480px;top:503px;width:113px;height:25px"></div>
<div class="abs field" style="left:633px;top:503px;width:113px;height:25px"></div>
<div class="abs field" style="left:480px;top:532px;width:266px;height:46px"></div>
<div class="abs submit">SUBMIT</div>

<h2 class="abs articles-title">LES DERNIERS ARTICLES</h2>

<article class="abs card" style="left:89px;top:707px">
  <div class="card-photo" role="img" aria-label="Photo d'une agente avec casque d'écoute prenant des notes" style="background:linear-gradient(135deg,#dfe8f0,#9aa9bb 60%,#2b3444)"></div>
  <h3>Et eros omnes theophrastus</h3>
  <p>Et eros omnes theophrastus mei, cumit usu dicit omnium eripuit. Qui tever illum facete, officiis gubergren sea cu.<br><a>Read more..</a></p>
</article>
<article class="abs card" style="left:429px;top:707px">
  <div class="card-photo" role="img" aria-label="Photo de mains tenant des documents près d'un clavier" style="top:18px;background:linear-gradient(135deg,#3b4f6b,#c9d3e0 50%,#2a2e36)"></div>
  <h3>Et eros omnes theophrastus</h3>
  <p>Et eros omnes theophrastus mei, cumit usu dicit omnium eripuit. Qui tever illum facete, officiis gubergren sea cu.<br><a>Read more..</a></p>
</article>
<article class="abs card" style="left:89px;top:878px">
  <div class="card-photo" role="img" aria-label="Photo d'un jeune homme souriant à son bureau" style="background:linear-gradient(135deg,#e9e4d8,#b89c7a 55%,#6e5a45)"></div>
  <h3>Et eros omnes theophrastus</h3>
  <p>Et eros omnes theophrastus mei, cumit usu dicit omnium eripuit. Qui tever illum facete, officiis gubergren sea cu.<br><a>Read more..</a></p>
</article>
<article class="abs card" style="left:429px;top:878px">
  <div class="card-photo" role="img" aria-label="Photo d'un cadre en réunion d'équipe" style="top:15px;background:linear-gradient(135deg,#e4ebf1,#9fb0c4 55%,#26344b)"></div>
  <h3>Et eros omnes theophrastus</h3>
  <p>Et eros omnes theophrastus mei, cumit usu dicit omnium eripuit. Qui tever illum facete, officiis gubergren sea cu.<br><a>Read more..</a></p>
</article>

<div class="abs follow-band"></div>
<div class="abs follow" style="left:97px">
  <div class="abs" style="left:72px;top:13px;width:18px;height:18px;background:#1f77b4"></div>
  <span style="left:108px">Suivez-nous sur notre réseau professionnel</span>
</div>
<div class="abs follow" style="left:443px">
  <svg class="abs" style="left:51px;top:12px" width="30" height="20" viewBox="0 0 30 20"><rect x="0.5" y="0.5" width="29" height="19" fill="#f4f4f4" stroke="#bbb"/><path d="M1 1 L15 11 L29 1" fill="none" stroke="#bbb"/></svg>
  <span style="left:107px;top:15px">Inscrivez-vous à l'infolettre</span>
</div>

<footer class="abs footer">
  <p>© Velnarix - Tous droits réservés</p>
  <span class="social" style="left:690px"></span>
  <span class="social" style="left:710px"></span>
  <span class="social" style="left:730px"></span>
  <span class="social" style="left:748px"></span>
</footer>

</body>
</html>
```